Business Card for plorvaTEC

Create a Business Card with an existing logo for plorvaTEC AG. We are a Information Technology company that does consulting and developing SW to automate business processes. The main colors are given from the logo.

Industry/Entity Type

Business

Requirements
Nice to have
• we use a a font style Century Gothic in our documents

```html
<!DOCTYPE html>
<html lang="en">
<head>
<meta charset="utf-8">
<title>plorvaTEC AG – Business Card</title>
<link rel="stylesheet" href="https://fonts.googleapis.com/css2?family=Questrial&display=swap">
<style>
  :root {
    --backdrop: #1c1c1c;
    --card: #ffffff;
    --ink: #333333;
    --text: #222222;
    --name-blue: #2b8fd8;
    --title-green: #7cc242;
    --bar-grey: #d3d4d6;
    --home-pink: #e8286f;
    --phone-orange: #f5901e;
    --web-black: #1e1e1e;
    --mail-teal: #17b3c8;
    --mark-green: #5cb83a;
  }
  html, body {
    margin: 0;
    width: 1200px;
    height: 758px;
    overflow: hidden;
    background: var(--backdrop);
    font-family: "Questrial", "Century Gothic", sans-serif;
  }
  .card {
    position: absolute;
    left: 100px;
    top: 89px;
    width: 1000px;
    height: 580px;
    background: var(--card);
  }
  .brand {
    position: absolute;
    left: 80px;
    top: 160px;
    display: flex;
    align-items: center;
    gap: 20px;
  }
  .brand-dot {
    width: 78px;
    height: 78px;
    border-radius: 50%;
    background: var(--mark-green);
  }
  .brand-name {
    font-size: 62px;
    color: var(--ink);
    letter-spacing: 1px;
  }
  .person {
    position: absolute;
    left: 120px;
    top: 372px;
    display: flex;
    flex-direction: column;
    align-items: flex-end;
  }
  .person-name {
    font-size: 46px;
    color: var(--name-blue);
    line-height: 1;
  }
  .person-title {
    font-size: 27px;
    color: var(--title-green);
    margin-top: 4px;
  }
  .contacts {
    position: absolute;
    left: 520px;
    top: 140px;
    margin: 0;
    padding: 0;
    list-style: none;
  }
  .contact {
    display: flex;
    align-items: center;
    height: 80px;
    margin-bottom: 16px;
  }
  .contact-icon {
    width: 80px;
    height: 80px;
    display: flex;
    align-items: center;
    justify-content: center;
    flex: none;
  }
  .contact-icon svg { width: 40px; height: 40px; }
  .icon-home { background: var(--home-pink); }
  .icon-phone { background: var(--phone-orange); }
  .icon-web { background: var(--web-black); }
  .icon-mail { background: var(--mail-teal); }
  .contact-text {
    margin-left: 12px;
    width: 340px;
    height: 70px;
    background: var(--bar-grey);
    display: flex;
    align-items: center;
    padding: 0 18px;
    box-sizing: border-box;
    font-size: 19px;
    line-height: 1.2;
    color: var(--text);
    white-space: nowrap;
  }
</style>
</head>
<body>
  <main class="card">
    <div class="brand">
      <span class="brand-dot"></span>
      <span class="brand-name">plorvaTEC</span>
    </div>

    <div class="person">
      <span class="person-name">Lukas Brenner</span>
      <span class="person-title">C.E.O</span>
    </div>

    <ul class="contacts">
      <li class="contact">
        <span class="contact-icon icon-home">
          <svg viewBox="0 0 40 40" aria-hidden="true"><path fill="#fff" d="M20 6 4 20h5v13h9v-9h4v9h9V20h5z"/></svg>
        </span>
        <span class="contact-text">Lindenhofweg 8, 4721 Varnholm,<br>Estravia</span>
      </li>
      <li class="contact">
        <span class="contact-icon icon-phone">
          <svg viewBox="0 0 40 40" aria-hidden="true"><path fill="#fff" d="M12 5c1.5 0 2.5 1 3 2.5l2 5c.5 1.4 0 2.6-1 3.4l-2 1.6c1.8 3.8 4.7 6.7 8.5 8.5l1.6-2c.8-1 2-1.5 3.4-1l5 2c1.5.5 2.5 1.5 2.5 3v4c0 1.8-1.5 3-3.2 3C16.6 34.5 5.5 23.4 5 8.2 5 6.5 6.2 5 8 5z"/></svg>
        </span>
        <span class="contact-text">+88 23 318 40 27<br>+88 67 462 85 90</span>
      </li>
      <li class="contact">
        <span class="contact-icon icon-web">
          <svg viewBox="0 0 40 40" aria-hidden="true" fill="none" stroke="#fff" stroke-width="2.4"><circle cx="20" cy="20" r="15"/><ellipse cx="20" cy="20" rx="6.5" ry="15"/><path d="M5 20h30M8 12h24M8 28h24"/></svg>
        </span>
        <span class="contact-text">www.plorvatec.com</span>
      </li>
      <li class="contact">
        <span class="contact-icon icon-mail">
          <svg viewBox="0 0 40 40" aria-hidden="true" fill="none" stroke="#fff" stroke-width="2.4"><rect x="5" y="10" width="30" height="20"/><path d="m5 10 15 12 15-12M5 30l11-10M35 30 24 20"/></svg>
        </span>
        <span class="contact-text">lukas.brenner@plorvatec.com</span>
      </li>
    </ul>
  </main>
</body>
</html>
```